Business Card Design

Needing a business card design similar to the business card that is attached.

Industry/Entity Type

Business

Contact Information for Business Card

Design similar to the b-cards that is attached.

```html
<!DOCTYPE html>
<html lang="en">
<head>
<meta charset="utf-8">
<title>Business Cards</title>
<link rel="stylesheet" href="https://fonts.googleapis.com/css2?family=Libre+Baskerville:wght@400;700&display=swap">
<style>
  :root {
    --bg: #e9e9e9;
    --card: #ffffff;
    --ink: #161616;
    --green: #2aa33a;
    --green-light: #8cc63f;
    --green-faint: #e3f1d6;
    --red: #e2352b;
    --blue: #1a8fc9;
    --blue-light: #5ab4e0;
    --blue-faint: #e4f1f8;
  }
  * { margin: 0; padding: 0; box-sizing: border-box; }
  html, body { width: 1200px; height: 1023px; overflow: hidden; }
  body {
    background: var(--bg);
    font-family: "Libre Baskerville", "Times New Roman", serif;
    color: var(--ink);
    position: relative;
  }
  .card {
    position: absolute;
    left: 250px;
    width: 700px;
    height: 400px;
    background: var(--card);
    border-radius: 18px;
    box-shadow: 0 6px 20px rgba(0,0,0,0.18);
    overflow: hidden;
  }
  .card--solar { top: 70px; }
  .card--realty { top: 553px; }

  .brand {
    position: absolute;
    left: 60px;
    top: 96px;
    display: flex;
    align-items: center;
    gap: 18px;
  }
  .brand__mark {
    width: 84px; height: 84px;
    border-radius: 50%;
  }
  .brand__name {
    font-weight: 700;
    font-size: 46px;
    letter-spacing: -0.5px;
    white-space: nowrap;
  }
  .card--solar .brand__mark { background: var(--green); }
  .card--solar .brand__name { color: var(--green); }
  .card--realty .brand__mark { background: var(--blue); border-radius: 6px; }
  .card--realty .brand__name { color: var(--red); }

  .deco {
    position: absolute;
    right: 26px;
    top: 40px;
    width: 130px; height: 130px;
    border-radius: 50%;
  }
  .card--solar .deco { background: var(--green-faint); }
  .card--realty .deco { background: var(--blue-faint); border-radius: 10px; }

  .rule {
    position: absolute;
    left: 300px;
    right: 0;
    top: 210px;
    border-top: 2px dashed;
  }
  .card--solar .rule { border-color: var(--green-light); }
  .card--realty .rule { border-color: var(--red); }

  .tab {
    position: absolute;
    left: 0;
    top: 228px;
    width: 16px;
    height: 28px;
    border-radius: 0 4px 4px 0;
  }
  .card--solar .tab { background: var(--green); }
  .card--realty .tab { background: var(--red); }

  .person {
    position: absolute;
    left: 60px;
    top: 224px;
    font-variant: small-caps;
  }
  .person__name { font-weight: 700; font-size: 22px; }
  .person__role { font-size: 15px; margin-top: 2px; }
  .card--solar .person__role { color: var(--green-light); }
  .card--realty .person__role { color: var(--blue-light); }

  .address {
    position: absolute;
    left: 60px;
    top: 290px;
    display: flex;
    gap: 12px;
    align-items: flex-end;
    font-weight: 700;
    font-size: 19px;
    line-height: 1.55;
  }
  .address__lines span { display: block; }
  .address__lines .city { font-variant: small-caps; }

  .contacts {
    position: absolute;
    left: 400px;
    top: 220px;
    list-style: none;
    font-weight: 700;
    font-size: 18px;
    line-height: 1.55;
  }
  .contacts li { display: flex; align-items: center; gap: 10px; }
  .contacts .web { font-variant: small-caps; }
  .icon { width: 18px; height: 18px; flex: none; }
  .card--solar .icon { fill: var(--green); stroke: var(--green); }
  .card--realty .icon { fill: var(--blue); stroke: var(--blue); }
</style>
</head>
<body>

<section class="card card--solar">
  <div class="deco"></div>
  <div class="brand">
    <span class="brand__mark"></span>
    <span class="brand__name">CascadeSun, Inc</span>
  </div>
  <div class="rule"></div>
  <span class="tab"></span>
  <div class="person">
    <div class="person__name">Daniel Asfaw</div>
    <div class="person__role">M.E &amp; Certified geothermal installer</div>
  </div>
  <ul class="contacts">
    <li>
      <svg class="icon" viewBox="0 0 24 24"><path stroke="none" d="M6.6 10.8a15 15 0 0 0 6.6 6.6l2.2-2.2c.3-.3.7-.4 1-.2 1.1.4 2.3.6 3.6.6.6 0 1 .4 1 1V20c0 .6-.4 1-1 1A17 17 0 0 1 3 4c0-.6.4-1 1-1h3.5c.6 0 1 .4 1 1 0 1.3.2 2.5.6 3.6.1.3 0 .7-.2 1z"/></svg>
      (206) 555-0148
    </li>
    <li>
      <svg class="icon" viewBox="0 0 24 24"><g fill="none" stroke-width="3"><rect x="3" y="9" width="10" height="6" rx="3" transform="rotate(-45 8 12)"/><rect x="11" y="9" width="10" height="6" rx="3" transform="rotate(-45 16 12)"/></g></svg>
      CascadeSunInc.com
    </li>
  </ul>
  <div class="address">
    <svg class="icon" viewBox="0 0 24 24"><path stroke="none" d="M12 2a7 7 0 0 0-7 7c0 5 7 13 7 13s7-8 7-13a7 7 0 0 0-7-7zm0 9.5A2.5 2.5 0 1 1 12 6.5a2.5 2.5 0 0 1 0 5z"/></svg>
    <div class="address__lines">
      <span>4820 S 201st Pl, #B200</span>
      <span class="city">Auburn, WA 98001</span>
    </div>
  </div>
</section>

<section class="card card--realty">
  <div class="deco"></div>
  <div class="brand">
    <span class="brand__mark"></span>
    <span class="brand__name">Summit Realty, Inc.</span>
  </div>
  <div class="rule"></div>
  <span class="tab"></span>
  <div class="person">
    <div class="person__name">Daniel Asfaw</div>
    <div class="person__role">Margj Broker</div>
  </div>
  <ul class="contacts">
    <li>
      <svg class="icon" viewBox="0 0 24 24"><path stroke="none" d="M6.6 10.8a15 15 0 0 0 6.6 6.6l2.2-2.2c.3-.3.7-.4 1-.2 1.1.4 2.3.6 3.6.6.6 0 1 .4 1 1V20c0 .6-.4 1-1 1A17 17 0 0 1 3 4c0-.6.4-1 1-1h3.5c.6 0 1 .4 1 1 0 1.3.2 2.5.6 3.6.1.3 0 .7-.2 1z"/></svg>
      (206) 555-0148
    </li>
    <li>
      <svg class="icon" viewBox="0 0 24 24"><rect stroke="none" x="4" y="8" width="16" height="13" rx="2"/><rect stroke="none" x="7" y="3" width="10" height="6"/></svg>
      (253) 555-0172
    </li>
    <li>
      <svg class="icon" viewBox="0 0 24 24"><g fill="none" stroke-width="3"><rect x="3" y="9" width="10" height="6" rx="3" transform="rotate(-45 8 12)"/><rect x="11" y="9" width="10" height="6" rx="3" transform="rotate(-45 16 12)"/></g></svg>
      <span class="web">SummitRealtyInc.com</span>
    </li>
  </ul>
  <div class="address">
    <svg class="icon" viewBox="0 0 24 24"><path stroke="none" d="M12 2a7 7 0 0 0-7 7c0 5 7 13 7 13s7-8 7-13a7 7 0 0 0-7-7zm0 9.5A2.5 2.5 0 1 1 12 6.5a2.5 2.5 0 0 1 0 5z"/></svg>
    <div class="address__lines">
      <span>4820 S 201st Pl, #B200</span>
      <span class="city">Auburn, WA 98001</span>
    </div>
  </div>
</section>

</body>
</html>
```